Executive & Leadership Coach needs a Graphic Design

We need a graphic design for a Leadership methodology/strategy that can be linked to The Summit Compass

The Summit Compass consists of:
1. Achievements
2. Personal Brand
3. Network
4. Executive Presence

This should Graphic Design will need to be used in PowerPoint presentations, training manuals and web pages

The design should be modern and provide the feeling of strength, trust, energy & creativity

Industry/Entity Type

Graphic Design

Font styles to use
Other font styles liked:
• Calibri, Verdana

```html
<!DOCTYPE html>
<html lang="en">
<head>
<meta charset="utf-8">
<title>The Summit Compass</title>
<link rel="stylesheet" href="https://fonts.googleapis.com/css2?family=Open+Sans:wght@700;800&display=swap">
<style>
  :root {
    --page-bg: #ffffff;
    --blue-deep: #1f6cbc;
    --blue-light: #29ade4;
    --green-lime: #8dc63f;
    --green-yellow: #e6e51c;
    --purple-light: #8a2d9c;
    --purple-deep: #5a2d8c;
    --pink-hot: #ec008c;
    --pink-rose: #e2185f;
    --chrome-light: #f4f4f5;
    --chrome-mid: #c4c6c9;
    --chrome-dark: #7f8287;
    --rim-shadow: #4a4b4e;
    --label: #ffffff;
    --hub-text-stroke: #555a60;
  }
  html, body {
    margin: 0;
    padding: 0;
    width: 1200px;
    height: 1000px;
    overflow: hidden;
    background: var(--page-bg);
  }
  .canvas {
    width: 1200px;
    height: 1000px;
    display: block;
  }
  .quadrant-label {
    font-family: "Open Sans", Verdana, sans-serif;
    font-weight: 800;
    font-size: 38px;
    fill: var(--label);
    letter-spacing: 0.5px;
  }
  .hub-title {
    font-family: "Open Sans", Verdana, sans-serif;
    font-weight: 700;
    font-size: 48px;
    stroke: var(--hub-text-stroke);
    stroke-width: 1.5px;
    paint-order: stroke;
  }
</style>
</head>
<body>
<svg class="canvas" viewBox="0 0 1200 1000" xmlns="http://www.w3.org/2000/svg" role="img" aria-label="The Summit Compass: Executive Presence, Achievements, Network and Personal">
  <defs>
    <linearGradient id="chrome-rim" x1="0" y1="0" x2="0" y2="1">
      <stop offset="0" stop-color="var(--chrome-mid)"/>
      <stop offset="0.25" stop-color="var(--chrome-light)"/>
      <stop offset="0.5" stop-color="var(--chrome-dark)"/>
      <stop offset="0.75" stop-color="var(--chrome-light)"/>
      <stop offset="1" stop-color="var(--chrome-mid)"/>
    </linearGradient>
    <linearGradient id="chrome-hub" x1="0" y1="0" x2="1" y2="1">
      <stop offset="0" stop-color="var(--chrome-light)"/>
      <stop offset="0.45" stop-color="var(--chrome-dark)"/>
      <stop offset="0.7" stop-color="var(--chrome-light)"/>
      <stop offset="1" stop-color="var(--chrome-mid)"/>
    </linearGradient>
    <radialGradient id="hub-face" cx="0.5" cy="0.4" r="0.6">
      <stop offset="0" stop-color="#ffffff"/>
      <stop offset="0.8" stop-color="#f3f3f3"/>
      <stop offset="1" stop-color="#d8d9db"/>
    </radialGradient>
    <linearGradient id="hub-text" x1="0" y1="0" x2="0" y2="1">
      <stop offset="0" stop-color="#e9eaec"/>
      <stop offset="0.5" stop-color="#8d9096"/>
      <stop offset="1" stop-color="#d7d8da"/>
    </linearGradient>
    <linearGradient id="fill-presence" x1="0" y1="0" x2="1" y2="1">
      <stop offset="0" stop-color="var(--blue-deep)"/>
      <stop offset="1" stop-color="var(--blue-light)"/>
    </linearGradient>
    <linearGradient id="fill-achievements" x1="0" y1="1" x2="1" y2="0">
      <stop offset="0" stop-color="var(--green-yellow)"/>
      <stop offset="0.6" stop-color="var(--green-lime)"/>
      <stop offset="1" stop-color="var(--green-lime)"/>
    </linearGradient>
    <linearGradient id="fill-network" x1="0" y1="1" x2="1" y2="0">
      <stop offset="0" stop-color="var(--purple-light)"/>
      <stop offset="1" stop-color="var(--purple-deep)"/>
    </linearGradient>
    <linearGradient id="fill-personal" x1="0" y1="1" x2="1" y2="0">
      <stop offset="0" stop-color="var(--pink-rose)"/>
      <stop offset="1" stop-color="var(--pink-hot)"/>
    </linearGradient>

    <!-- top labels: baseline on arc, letters grow outward -->
    <path id="arc-presence" d="M 312,500 A 288 288 0 0 1 600,212"/>
    <path id="arc-achievements" d="M 600,212 A 288 288 0 0 1 888,500"/>
    <!-- bottom labels: baseline on arc, letters grow inward toward the hub -->
    <path id="arc-personal" d="M 290,500 A 310 310 0 0 0 600,810"/>
    <path id="arc-network" d="M 600,810 A 310 310 0 0 0 910,500"/>
  </defs>

  <g class="compass-wheel">
    <circle class="rim-depth" cx="600" cy="512" r="372" fill="var(--rim-shadow)"/>
    <circle class="rim" cx="600" cy="500" r="372" fill="url(#chrome-rim)" stroke="#9a9ca0" stroke-width="2"/>
    <circle class="rim-inner-edge" cx="600" cy="500" r="338" fill="#ffffff"/>

    <g class="quadrants">
      <path class="quadrant quadrant--presence" d="M600,500 L265,500 A335 335 0 0 1 600,165 Z" fill="url(#fill-presence)"/>
      <path class="quadrant quadrant--achievements" d="M600,500 L600,165 A335 335 0 0 1 935,500 Z" fill="url(#fill-achievements)"/>
      <path class="quadrant quadrant--network" d="M600,500 L935,500 A335 335 0 0 1 600,835 Z" fill="url(#fill-network)"/>
      <path class="quadrant quadrant--personal" d="M600,500 L600,835 A335 335 0 0 1 265,500 Z" fill="url(#fill-personal)"/>
      <line class="divider" x1="600" y1="165" x2="600" y2="835" stroke="#ffffff" stroke-width="2.5"/>
      <line class="divider" x1="265" y1="500" x2="935" y2="500" stroke="#ffffff" stroke-width="2.5"/>
    </g>

    <g class="quadrant-labels">
      <text class="quadrant-label"><textPath href="#arc-presence" startOffset="50%" text-anchor="middle">Executive Presence</textPath></text>
      <text class="quadrant-label"><textPath href="#arc-achievements" startOffset="50%" text-anchor="middle">Achievements</textPath></text>
      <text class="quadrant-label"><textPath href="#arc-personal" startOffset="50%" text-anchor="middle">Personal</textPath></text>
      <text class="quadrant-label"><textPath href="#arc-network" startOffset="50%" text-anchor="middle">Network</textPath></text>
    </g>

    <g class="hub">
      <circle class="hub-shadow" cx="600" cy="506" r="150" fill="rgba(0,0,0,0.25)"/>
      <circle class="hub-ring" cx="600" cy="500" r="148" fill="url(#chrome-hub)" stroke="#8c8f94" stroke-width="1.5"/>
      <circle class="hub-face" cx="600" cy="500" r="122" fill="url(#hub-face)" stroke="#b9bbbf" stroke-width="1.5"/>
      <text class="hub-title" x="600" y="490" text-anchor="middle" fill="url(#hub-text)">Summit</text>
      <text class="hub-title" x="600" y="550" text-anchor="middle" fill="url(#hub-text)">Compass</text>
    </g>
  </g>
</svg>
</body>
</html>
```